Flyer Design for International Business Consultant

We need an advertisement to help build the profile of Colin Marsh, Senior Consultant and Director at 'LUPE Advisory Group'.

What we want to promote:
Our Senior Consultant and Director, Colin Marsh as expert on all matters China related.

Who are we promoting to:
Industry associations and networking groups.

Why:
Many organisations are interested in reaching the Chinese market, however don't know who to go to or who to trust. With many consultants out there trying to claim they offer a similar service, LUPE would like to promote Colin as a genuine expert in the field and the 'go to' person on all things China business related. To do this, we are in the process of building Colin's national and international profile, which includes advertising Colin expertise to industry associations and networking groups so that they consider booking Colin as a key note speaker at conferences. We know that our target audience are more inclined to seek the advice of someone they have seen speak at a conference than to find someone in the Blue listings or via findly search.

A Bit about Colin Marsh:

Colin Marsh has lived, worked and studied in China for extended periods, speaks and writes fluently in Chinese, was formerly a Member of the Regional Trade Outreach Steering Panel, is a member of the Institute of Cross-Border Commerce and is a member of the Pacific Trade Partners Forum to name a few. To add to his credentials, Colin has by invitation lectured for 5 consecutive years in Management and Economics at Masters Level to students at Harbourline Institute.

Colin’s qualifications include: Bachelor of Arts (Asian Studies), Bachelor of Business (Applied Economics – International Trade), Master of Business in Applied Economics (International Business) and currently completing a Doctor of Business Administration (International Business Management) which has an economics focus and researches the export of Australian professional services to China.

Colin has been the Principal Consultant for a number of LUPE’s clients including the recent assignment commissioned by Victorian based company Bremo Freight, who have benefited from a $40 million deal with Eastern Iron Works (EIW). This project has also resulted in EIW, China’s largest train manufacturer decision to set up offices in Victoria.

Colin is an expert in Australia/China Business relations and has been paramount to the success of numerous international business transactions. As mentioned, Colin is not only fluent in spoken and written Mandarin, but is also a bi-cultural expert (meaning he knows both Australian and Chinese) cultures. From Australian and Chinese history, art, food and more, Colin Marsh provides his clients with more than translation services.

A Bit about LUPE Advisory Group:

Run by experienced business executives with over 20 years’ experience in the Chinese and Australian markets, LUPE brings a un-paralleled level of knowledge and expertise that enables cooperative business relations to develop between international organisations despite the language and cultural differences. They are a bi-lingual and bi-cultural international business consultancy that specialise in managing cross-border business involving China.

LUPE has expertise in all facets of business management and has worked with a range of companies and organisations to develop and implement strategic business solutions to set direction, improve performance and maximise returns to stakeholders. LUPE has particular expertise in economic and market analysis and specialises in project management of large and complex projects, strategic procurement, market research and market development strategies. Combined with their cultural and language skills, LUPE provides a unique and high value contribution to international projects.
Updates

Good afternoon designers

Thank you for your submissions so far.  We are happy with some of the designs that have come in, however, many of you have produced flyers that have too much information in it.  We are looking for something more concise that does not appear to be either a copy of information I have posted in this brief or a fancy looking resume for Colin Marsh. 

Please remember, we are communicating to event co-ordinators who are looking to appoint guest speakers at an upcoming conference.  They want someone who is going to discuss some of the 'hot topics' their audience are interested in, someone who is experienced in the topic and someone who is interesting. We need to communicate all of this in a concise, and creative way so that we can make Colin Marsh stand out above the rest.

Dear Designers

Thank you all very much for your submissions.  We appreciate you taking the time to compose a flyer for our organisation. 

Regards
Tessa

Dear Designers

Regards
Tessa

Target Market(s)

Event/conference managers or coordinators

Industry/Entity Type

Business Management

Requirements
Must have
• Must have the LUPE Logo on it (red, white and black). The ad will be in the form of an electronic flyer to be embedded in an email that will be sent on to relevant contacts in our database.

```html
<!DOCTYPE html>
<html lang="en">
<head>
<meta charset="utf-8">
<title>Colin Marsh – Keynote Speaker Flyer</title>
<link href="https://fonts.googleapis.com/css2?family=Noto+Sans+TC:wght@500&family=Oswald:wght@500;600&family=Open+Sans:wght@400;600&display=swap" rel="stylesheet">
<style>
  :root {
    --paper: #f4f3f1;
    --paper-edge: #e4e2df;
    --ink: #1c1c1c;
    --red: #c8161d;
    --red-dark: #a50f15;
    --note-red: #d9534f;
    --grey: #555555;
    --body: #4a4a4a;
    --white: #ffffff;
  }
  * { box-sizing: border-box; margin: 0; padding: 0; }
  html, body { width: 849px; height: 1200px; overflow: hidden; }
  body {
    background: radial-gradient(ellipse at 50% 30%, var(--white) 0%, var(--paper) 60%, var(--paper-edge) 100%);
    font-family: "Open Sans", Arial, sans-serif;
    color: var(--ink);
    position: relative;
  }
  .headline-zh {
    position: absolute;
    top: 76px;
    left: 0;
    width: 849px;
    text-align: center;
    font-family: "Noto Sans TC", sans-serif;
    font-weight: 500;
    font-size: 100px;
    line-height: 110px;
    letter-spacing: 2px;
    color: var(--ink);
  }
  .annotation {
    position: absolute;
    background: var(--note-red);
    opacity: 0.18;
    border-radius: 4px;
  }
  .tear-band {
    position: absolute;
    top: 440px;
    left: 0;
    width: 849px;
    height: 190px;
  }
  .tear-band svg { position: absolute; inset: 0; }
  .tear-band__text {
    position: absolute;
    top: 44px;
    width: 100%;
    text-align: center;
    font-family: "Oswald", sans-serif;
    font-weight: 600;
    font-size: 40px;
    line-height: 50px;
    color: var(--white);
    text-transform: uppercase;
    letter-spacing: 0.5px;
  }
  .subhead {
    position: absolute;
    top: 672px;
    left: 60px;
    width: 729px;
    text-align: center;
    font-family: "Oswald", sans-serif;
    font-weight: 500;
    font-size: 23px;
    line-height: 30px;
    color: var(--grey);
    text-transform: uppercase;
  }
  .bio {
    position: absolute;
    top: 742px;
    left: 85px;
    width: 680px;
    font-size: 12.6px;
    line-height: 19px;
    text-align: justify;
    color: var(--body);
  }
  .booking {
    position: absolute;
    top: 884px;
    left: 85px;
    width: 680px;
    font-size: 14px;
    color: var(--body);
  }
  .footer-address {
    position: absolute;
    top: 1140px;
    left: 215px;
    width: 420px;
    font-size: 11.5px;
    line-height: 16px;
    color: var(--grey);
    white-space: nowrap;
  }
  .brand {
    position: absolute;
    top: 1100px;
    left: 660px;
    display: flex;
    align-items: center;
    gap: 10px;
  }
  .brand__mark {
    width: 50px;
    height: 50px;
    background: var(--red);
  }
  .brand__name {
    font-family: "Oswald", sans-serif;
    font-weight: 500;
    font-size: 18px;
    line-height: 21px;
    color: var(--ink);
    text-transform: uppercase;
  }
</style>
</head>
<body>

  <div class="annotation" style="top:30px;left:40px;width:110px;height:58px" role="img" aria-label="Handwritten red notes around the Chinese headline"></div>
  <div class="annotation" style="top:32px;left:640px;width:150px;height:48px" role="img" aria-label="Handwritten red notes"></div>
  <div class="annotation" style="top:312px;left:40px;width:300px;height:70px" role="img" aria-label="Handwritten red notes below the headline"></div>
  <div class="annotation" style="top:318px;left:560px;width:240px;height:70px" role="img" aria-label="Handwritten red notes below the headline"></div>

  <h1 class="headline-zh" lang="zh-Hant">你的產品是在<br>蘇州工業園區</h1>

  <section class="tear-band">
    <svg width="849" height="190" viewBox="0 0 849 190" aria-hidden="true">
      <polygon fill="var(--red)" points="0,14 40,8 90,18 140,6 200,15 260,4 320,16 380,7 440,17 500,5 560,14 620,6 680,18 740,8 800,15 849,6 849,180 800,172 750,186 690,174 630,184 570,171 510,185 450,173 390,186 330,172 270,184 210,171 150,186 90,173 40,184 0,174"/>
      <polyline fill="none" stroke="var(--red-dark)" stroke-width="3" points="0,14 40,8 90,18 140,6 200,15 260,4 320,16 380,7 440,17 500,5 560,14 620,6 680,18 740,8 800,15 849,6"/>
    </svg>
    <p class="tear-band__text">There are a lot more like him<br>in need of more than just a translator</p>
  </section>

  <h2 class="subhead">So it would be senseless not to hear what Colin Marsh has<br>to say on international business relations with China</h2>

  <p class="bio">Colin Marsh is senior consultant at LUPE Advisory Group and expert in Australia/China Business relations. His success of numerous international business transactions has exceeded expectations. Colin has been the Principal Consultant for a number of LUPE’s clients including the recent assignment commissioned by Victorian based company Bremo Freight, who have benefited from a $40 million deal with Eastern Iron Works. Colin lived, worked and studied in China for extended periods making him fluent in spoken and written Mandarin, making him a bi-cultural expert on Australian and Chinese culture.</p>

  <p class="booking">To book Colin Marsh as key speaker at a conference please contact us on: 000000000</p>

  <p class="footer-address">Business Consultants 12 Harlow Lane, Kensington VIC 3031, Australia</p>

  <div class="brand">
    <div class="brand__mark"></div>
    <div class="brand__name">LUPE<br>Advisory Group</div>
  </div>

</body>
</html>
```